Heating and Air Conditioning Company Needs a Business Card Design

Need a business card design for a company in South Carolina called "Larkfield Heating & Cooling LLC". We install, maintain, and repair HVAC systems and the bulk of our business is residential. We have a logo and are looking for a clean, professional looking card that resonates with "setting the standard for service and comfort".
Updates
Forgot to include this info - Licensed & Insured

Industry/Entity Type
Business

```html
<!DOCTYPE html>
<html lang="en">
<head>
<meta charset="utf-8">
<title>Larkfield Heating &amp; Cooling LLC — Business Card</title>
<link rel="stylesheet" href="https://fonts.googleapis.com/css2?family=Open+Sans:wght@400;600;700;800&display=swap">
<style>
  :root {
    --page-bg: #e9e6e1;
    --white: #ffffff;
    --blue-deep: #1c3f9e;
    --blue-mid: #2456c4;
    --blue-light: #2f8fe3;
    --orange: #f39a1b;
    --orange-deep: #e8750d;
    --ink: #1f2a44;
    --text-light: #e8f1ff;
  }
  * { box-sizing: border-box; margin: 0; padding: 0; }
  html, body {
    width: 1200px; height: 1024px; overflow: hidden;
    background: var(--page-bg);
    font-family: "Open Sans", Arial, sans-serif;
  }
  .card {
    position: absolute;
    left: 250px;
    width: 700px; height: 400px;
    border-radius: 30px;
    overflow: hidden;
    box-shadow: 0 14px 30px rgba(0,0,0,0.18);
  }
  .card--front { top: 92px; background: var(--white); }
  .card--back {
    top: 534px;
    background: radial-gradient(ellipse at 35% 40%, var(--blue-mid) 0%, var(--blue-deep) 75%);
  }
  .card__shape { position: absolute; inset: 0; width: 100%; height: 100%; }

  .brand { position: absolute; }
  .brand__row { display: flex; align-items: center; gap: 12px; }
  .brand__dot { width: 34px; height: 34px; border-radius: 50%; flex: none; }
  .brand__name {
    font-weight: 800; font-size: 44px; letter-spacing: 0.5px;
    line-height: 1; text-transform: uppercase;
  }
  .brand__sub {
    font-weight: 800; font-size: 19px; letter-spacing: 0.4px;
    margin-top: 6px; margin-left: 46px;
  }
  .card--front .brand { left: 34px; top: 160px; color: var(--ink); }
  .card--front .brand__dot { background: var(--blue-mid); }
  .card--back .brand { left: 130px; top: 120px; color: var(--white); }
  .card--back .brand__dot { background: var(--orange); }

  .contact {
    position: absolute; left: 430px; top: 52px; width: 250px;
    color: var(--white);
  }
  .contact__name { font-weight: 700; font-size: 17px; letter-spacing: 0.5px; text-transform: uppercase; }
  .contact__role { font-weight: 600; font-size: 12px; color: var(--text-light); margin-bottom: 22px; }
  .contact__address { font-size: 14px; line-height: 1.45; margin-bottom: 20px; }
  .contact__line {
    display: flex; align-items: center; gap: 10px;
    font-size: 14px; line-height: 1; margin-bottom: 8px;
  }
  .contact__line--web { margin-top: 16px; }
  .icon { width: 14px; height: 14px; flex: none; }

  .services {
    position: absolute; left: 176px; top: 230px;
    color: var(--text-light); font-size: 15px; line-height: 1.6; letter-spacing: 0.3px;
  }
</style>
</head>
<body>

  <section class="card card--front" aria-label="Business card front">
    <svg class="card__shape" viewBox="0 0 700 400" preserveAspectRatio="none" aria-hidden="true">
      <defs>
        <linearGradient id="panelBlue" x1="0" y1="0" x2="1" y2="1">
          <stop offset="0" stop-color="#1d45a8"/>
          <stop offset="0.55" stop-color="#2f8fe3"/>
          <stop offset="1" stop-color="#1c3f9e"/>
        </linearGradient>
        <linearGradient id="bandOrange" x1="0" y1="0" x2="0" y2="1">
          <stop offset="0" stop-color="#f7b12a"/>
          <stop offset="1" stop-color="#e8750d"/>
        </linearGradient>
      </defs>
      <path d="M318 0 C 410 70, 430 300, 350 400 L 378 400 C 460 300, 440 70, 350 0 Z" fill="url(#bandOrange)"/>
      <path d="M352 0 C 444 70, 462 300, 380 400 L 700 400 L 700 0 Z" fill="url(#panelBlue)"/>
    </svg>

    <div class="brand">
      <div class="brand__row">
        <span class="brand__dot"></span>
        <span class="brand__name">Larkfield</span>
      </div>
      <div class="brand__sub">Heating &amp; Cooling LLC</div>
    </div>

    <div class="contact">
      <p class="contact__name">Dale Hensley</p>
      <p class="contact__role">Certified Technician</p>
      <p class="contact__address">245 Maple Ridge Road,<br>Laurens, SC 29360</p>
      <p class="contact__line">
        <svg class="icon" viewBox="0 0 16 16" aria-hidden="true"><circle cx="8" cy="8" r="8" fill="var(--orange)"/><path d="M5 4.5l2 0 .6 2-1 .8a5 5 0 0 0 2.1 2.1l.8-1 2 .6 0 2c-3.5.4-7-3-6.5-6.5z" fill="#fff"/></svg>
        (555) 010-2145
      </p>
      <p class="contact__line">
        <svg class="icon" viewBox="0 0 16 16" aria-hidden="true"><circle cx="8" cy="8" r="8" fill="var(--orange)"/><rect x="4.5" y="6" width="7" height="5" fill="#fff"/><rect x="6" y="3.8" width="4" height="2.2" fill="#fff"/></svg>
        (555) 010-2146
      </p>
      <p class="contact__line">
        <svg class="icon" viewBox="0 0 16 16" aria-hidden="true"><circle cx="8" cy="8" r="8" fill="var(--orange)"/><rect x="5.5" y="3.5" width="5" height="9" rx="1" fill="#fff"/></svg>
        (555) 010-3380
      </p>
      <p class="contact__line contact__line--web">
        <svg class="icon" viewBox="0 0 16 16" aria-hidden="true"><circle cx="8" cy="8" r="8" fill="var(--orange)"/><rect x="4" y="5" width="8" height="6" fill="#fff"/><path d="M4 5l4 3.2L12 5" stroke="var(--orange)" fill="none"/></svg>
        dale@larkfieldhc.net
      </p>
      <p class="contact__line">
        <svg class="icon" viewBox="0 0 16 16" aria-hidden="true"><circle cx="8" cy="8" r="8" fill="var(--orange)"/><circle cx="8" cy="8" r="4" fill="none" stroke="#fff"/><path d="M4 8h8M8 4v8" stroke="#fff"/></svg>
        www.larkfieldhc.net
      </p>
    </div>
  </section>

  <section class="card card--back" aria-label="Business card back">
    <div class="brand">
      <div class="brand__row">
        <span class="brand__dot"></span>
        <span class="brand__name">Larkfield</span>
      </div>
      <div class="brand__sub">Heating &amp; Cooling LLC</div>
    </div>
    <p class="services">Heating • Cooling • Plumbing<br>Residential • Commercial • Industrial</p>
  </section>

</body>
</html>
```